Flyer for Car Detailing Shop

I am opening a detailing shop. I am looking for a nice, easy to read single sided flyer I can hand out at car shows, hang in store windows and to my clients and customers to promote my business. I want it a little professional yet attention grabbing. I want someone to look at it and go "holy shit, thats a nice flyer" haha

Here are some things that must be included:
- Company Name: Brightfern Motorworks Detailing & Coatings
- Tag Line: The Science of Detailing
- Address: 4150 Harlow Rd, Temperance, MI 48190
- www.brightfernmotor.example
- Find Us on social Media! ::insert facebook and instagram logo
Colors: Black, Lime Green and Purple for accents, etc

HAND WASH
- Express Wash start at $25
- Deluxe Wash Start at $50

EXTERIOR DETAILING
-Basic Packages Start at $160
- Deluxe Packages Start at $350

INTERIOR DETAILING
- Basic Packages Start at $60
- Deluxe Packages Start at $200

New Car Prep and Ceramic Coatings
*Consultation required prior to beginning work*
- Paint: Starting at $500
- Interior: Starting at $100
- Wheels Off: Starting at $200
- Trim: Starting at $100
- Windows: $50 windshield/ $25 per pane

Additional Services
- Scratch removal
- Ozone Treatment
- Headlight Restoration
- Chip Repair

```html
<!DOCTYPE html>
<html lang="en">
<head>
<meta charset="utf-8">
<title>Brightfern Motorworks Detailing &amp; Coatings Flyer</title>
<link rel="stylesheet" href="https://fonts.googleapis.com/css2?family=Bebas+Neue&family=Share+Tech+Mono&family=Source+Code+Pro:wght@500;700&display=swap">
<style>
  :root {
    --page-bg: #e9e9e9;
    --flyer-black: #050505;
    --lime: #8ab92d;
    --white: #ececec;
    --purple-deep: #5a1d86;
    --purple-blue: #4a3e9f;
    --panel-line: #b9a5de;
    --ink: #0c0c0c;
  }
  * { box-sizing: border-box; margin: 0; padding: 0; }
  html, body { width: 1180px; height: 1200px; overflow: hidden; background: var(--page-bg); }
  .flyer {
    position: absolute; left: 145px; top: 20px; width: 890px; height: 1160px;
    background: var(--flyer-black); overflow: hidden;
  }
  .headline {
    position: absolute; left: 79px; top: 66px;
    font-family: "Bebas Neue", sans-serif; font-size: 100px; line-height: 90px;
    color: var(--white); letter-spacing: 0;
  }
  .headline .accent { color: var(--lime); display: block; }
  .brand-badge {
    position: absolute; left: 557px; top: 62px; width: 270px; height: 270px; border-radius: 50%;
    background: #f1f1f1; border: 4px solid transparent;
    background-image: linear-gradient(#f1f1f1, #f1f1f1), linear-gradient(135deg, var(--purple-deep), var(--lime));
    background-origin: border-box; background-clip: padding-box, border-box;
    display: flex; flex-direction: column; align-items: center; justify-content: center; text-align: center;
    font-family: "Bebas Neue", sans-serif; font-size: 30px; line-height: 32px; color: var(--ink);
  }
  .car-photo {
    position: absolute; left: 83px; top: 370px; width: 738px; height: 293px;
    background: radial-gradient(ellipse at 50% 55%, #3a3a3a 0%, #1c1c1c 45%, #050505 75%);
  }
  .price-panel {
    position: absolute; left: 52px; top: 704px; width: 787px; height: 287px;
    border-radius: 22px; border: 2px solid var(--panel-line);
    background: linear-gradient(100deg, var(--purple-deep), var(--purple-blue));
    color: var(--white);
  }
  .divider-v { position: absolute; left: 443px; top: 0; width: 1px; height: 223px; background: var(--panel-line); }
  .divider-h { position: absolute; left: 0; right: 0; top: 223px; height: 1px; background: var(--panel-line); }
  .label {
    position: absolute; font-family: "Bebas Neue", sans-serif; font-size: 21px; line-height: 22px;
    letter-spacing: 0.3px; text-align: right; white-space: nowrap;
  }
  .item {
    position: absolute; font-family: "Share Tech Mono", monospace; font-size: 14.5px; line-height: 18px; white-space: nowrap;
  }
  .coat-title { position: absolute; left: 461px; top: 24px; font-family: "Bebas Neue", sans-serif; font-size: 21px; white-space: nowrap; }
  .coat-note { position: absolute; left: 461px; top: 46px; font-family: "Share Tech Mono", monospace; font-size: 10px; white-space: nowrap; }
  .coat-line { position: absolute; left: 461px; font-family: "Share Tech Mono", monospace; font-size: 15px; white-space: nowrap; }
  .address-bar {
    position: absolute; left: 66px; top: 1012px; width: 757px; height: 34px; border-radius: 17px;
    background: var(--lime); color: var(--ink);
    font-family: "Source Code Pro", monospace; font-weight: 500; font-size: 20px; line-height: 34px; text-align: center;
  }
  .website {
    position: absolute; left: 63px; top: 1056px; width: 535px;
    font-family: "Bebas Neue", sans-serif; font-size: 46px; line-height: 50px; color: var(--white);
    letter-spacing: 0.3px; white-space: nowrap;
  }
  .social-note {
    position: absolute; left: 613px; top: 1060px; color: var(--lime);
    font-family: "Source Code Pro", monospace; font-weight: 700; font-size: 15px; line-height: 19px; white-space: nowrap;
  }
  .social-icon { position: absolute; top: 1063px; width: 32px; height: 32px; border-radius: 6px; background: var(--white); }
</style>
</head>
<body>
<main class="flyer">
  <h1 class="headline">The<br>Science of<span class="accent">Detailing</span></h1>

  <div class="brand-badge">Brightfern<br>Motorworks<br>Detailing &amp; Coatings</div>

  <div class="car-photo" role="img" aria-label="Photo of a glossy black luxury coupe against a dark background"></div>

  <section class="price-panel">
    <div class="divider-v"></div>
    <div class="divider-h"></div>

    <div class="label" style="right:617px;top:25px;">Hand Washing &gt;</div>
    <div class="item" style="left:178px;top:24px;">Express Wash<br>start at $25</div>
    <div class="item" style="left:307px;top:24px;">Deluxe Wash<br>start at $50</div>

    <div class="label" style="right:617px;top:100px;">Exterior Detailing &gt;</div>
    <div class="item" style="left:178px;top:99px;">Basic Packages<br>start at $160</div>
    <div class="item" style="left:307px;top:99px;">Deluxe Packages<br>start at $350</div>

    <div class="label" style="right:617px;top:171px;">Interior Detailing &gt;</div>
    <div class="item" style="left:178px;top:170px;">Basic Packages<br>start at $60</div>
    <div class="item" style="left:307px;top:170px;">Deluxe Packages<br>start at $200</div>

    <div class="coat-title">New Car Prep and Ceramic Coatings</div>
    <div class="coat-note">*Consultation required prior to beginning work*</div>
    <div class="coat-line" style="top:78px;">Paint: Starting at $500</div>
    <div class="coat-line" style="top:105px;">Interior: Starting at $100</div>
    <div class="coat-line" style="top:133px;">Wheels Off: Starting at $200</div>
    <div class="coat-line" style="top:160px;">Trim: Starting at $100</div>
    <div class="coat-line" style="top:188px;">Windows: $50 windshield/ $25 per pane</div>

    <div class="label" style="right:572px;top:245px;">Additional Services &gt;</div>
    <div class="item" style="left:237px;top:238px;">Scratch<br>removal</div>
    <div class="item" style="left:361px;top:238px;">Ozone<br>Treatment</div>
    <div class="item" style="left:518px;top:238px;">Headlight<br>Restoration</div>
    <div class="item" style="left:683px;top:238px;">Chip<br>Repair</div>
  </section>

  <div class="address-bar">4150 Harlow Rd, Temperance, MI 48190</div>
  <div class="website">WWW.BRIGHTFERNMOTOR.EXAMPLE</div>
  <div class="social-note">Find Us on<br>social Media!</div>
  <div class="social-icon" style="left:743px;" aria-label="Social media link"></div>
  <div class="social-icon" style="left:783px;" aria-label="Social media link"></div>
</main>
</body>
</html>
```